Redesign of the current website

We would like a new format and redesign of the www.getorva.com website. We are a medical tech company and want our site to reflect current technology trends. TORVA provides innovative solutions to streamline business operations of Imaging Providers and Physicians while delivering life-changing solutions to patients. Free to patients and physicians.

Target Market(s)

Imaging Providers (with a secondary appeal for physicians and patients)

Industry/Entity Type

MedTech

Coding

Coded - Design and coding required

Number of Pages Required

1 page

Font styles to use
Sans Serif

Requirements
Must have
• New clear slogan to represent who and what we do.
Nice to have
• TORVA provides innovative solutions to streamline business operations of Imaging Providers and Physicians while delivering life-changing solutions to patients.
Should not have
• Social Radiology or Join the revolution

```html
<!DOCTYPE html>
<html lang="en">
<head>
<meta charset="utf-8">
<title>TORVA – Empower Patients &amp; Healthcare Providers</title>
<link href="https://fonts.googleapis.com/css2?family=Montserrat:wght@400;500;600;700&display=swap" rel="stylesheet">
<style>
:root{
  --teal:#27b3d6;
  --green:#8cc63f;
  --dark:#2f2f2f;
  --ink:#222;
  --text:#666;
  --light:#f3f3f3;
  --line:#e4e4e4;
  --grad:linear-gradient(90deg,#27b3d6,#8cc63f);
}
*{box-sizing:border-box;margin:0;padding:0}
html,body{width:1200px;height:4481px;overflow:hidden}
body{font-family:'Montserrat',sans-serif;color:var(--text);background:#fff;position:relative}
section,header,footer{position:absolute;left:0;width:1200px}
.abs{position:absolute}
.center{text-align:center;left:0;width:1200px}
.eyebrow{font-size:9px;letter-spacing:3px;color:var(--green);font-weight:600;text-transform:uppercase}
.h2{font-size:25px;font-weight:600;color:var(--ink);text-transform:uppercase;line-height:31px}
.lead{font-size:10.5px;line-height:16px;color:var(--text)}
.btn{display:inline-block;background:var(--grad);color:#fff;font-size:9px;font-weight:600;letter-spacing:1px;padding:8px 18px;border-radius:20px;text-transform:uppercase}
.bubble{position:absolute;left:572px;width:56px;height:56px;border-radius:50%;background:#fff;box-shadow:0 3px 10px rgba(0,0,0,.12);display:flex;align-items:center;justify-content:center}
.bubble span{width:26px;height:16px;border-radius:10px;background:var(--grad)}
.ph{position:absolute}

/* header */
.hero{top:0;height:591px;background:linear-gradient(120deg,#3a3f44 0%,#8a8e92 45%,#c7c3bd 70%,#6b6c6e 100%)}
.nav{position:absolute;top:28px;left:0;width:1200px;height:24px}
.logo{position:absolute;left:128px;top:0;font-size:24px;font-weight:700;color:var(--green);display:flex;align-items:center;gap:6px}
.logo i{width:12px;height:12px;border-radius:50%;background:var(--teal);display:block}
.menu{position:absolute;left:522px;top:6px;display:flex;gap:20px;font-size:9px;font-weight:600;color:#fff}
.menu .on{color:var(--teal)}
.phone{position:absolute;left:842px;top:6px;font-size:9px;color:#fff;font-weight:600}
.login{position:absolute;left:948px;top:0;padding:6px 14px;border-radius:14px;background:var(--teal);color:#fff;font-size:9px;font-weight:600}
.hero h1{position:absolute;top:232px;font-size:32px;line-height:38px;font-weight:600;color:#fff;text-transform:uppercase}
.hero .tag{top:210px;font-size:9px;letter-spacing:3px;color:#fff}
.hero .tag b{color:var(--teal);font-weight:600}
.hero .sub{top:315px;font-size:10.5px;line-height:16px;color:#fff}
.hero .cta{top:364px}
.scroll{position:absolute;left:584px;top:540px;width:24px;height:24px;border-radius:50%;background:rgba(0,0,0,.35)}

/* thinking ahead */
.think{top:591px;height:374px}
.think .pic{left:129px;top:63px;width:461px;height:258px;background:linear-gradient(135deg,#0d1a2c,#2c4f6e 55%,#0b1522)}
.play{position:absolute;left:563px;top:165px;width:54px;height:54px;border-radius:50%;background:#fff;box-shadow:0 2px 8px rgba(0,0,0,.2)}
.play:after{content:"";position:absolute;left:23px;top:19px;border-left:11px solid var(--teal);border-top:8px solid transparent;border-bottom:8px solid transparent}
.think .copy{left:647px;top:85px;width:350px}
.think h3{font-size:24px;font-weight:600;color:var(--ink);margin:12px 0 16px}
.think p{font-size:10px;line-height:15px;margin-bottom:10px}

/* approach */
.approach{top:965px;height:273px}
.steps{position:absolute;top:75px;left:120px;width:960px;display:flex}
.step{width:160px;text-align:center;font-size:9.5px;line-height:13px}
.step .ic{width:52px;height:52px;border-radius:50%;background:var(--dark);margin:0 auto 10px;display:flex;align-items:center;justify-content:center}
.step .ic.active{border:3px solid var(--green);color:#fff;font-size:18px;font-weight:600}
.step .ic span{width:18px;height:18px;border:2px solid #fff;border-radius:3px}
.step b{display:block;color:var(--teal);font-weight:600;margin-bottom:2px}

/* solution */
.solution{top:1238px;height:727px;background:linear-gradient(#fff,var(--light) 30%)}
.cards{position:absolute;top:245px;left:129px;display:flex;gap:19px}
.card{position:relative;width:301px;height:401px}
.card.photo1{background:linear-gradient(160deg,#d8dde0,#8d979d)}
.card.photo2{background:linear-gradient(160deg,#c5c9c9,#6e7472)}
.card.mid{background:#3c3c3c;color:#fff;padding:40px 28px}
.card .lbl{position:absolute;bottom:42px;width:100%;text-align:center;color:#fff;font-size:10px;font-weight:700}
.card .dot{position:absolute;bottom:-18px;left:128px;width:44px;height:44px;border-radius:50%;background:#fff;box-shadow:0 2px 6px rgba(0,0,0,.15)}
.card h4{text-align:center;font-size:15px;font-weight:700;margin:18px 0 12px}
.card ul{list-style:none;font-size:9.5px;line-height:12px}
.card li{padding-left:14px;position:relative;margin-bottom:6px}
.card li:before{content:"";position:absolute;left:0;top:2px;width:6px;height:6px;border:1px solid var(--teal);border-radius:50%}
.card .mini{position:absolute;left:135px;bottom:28px;width:30px;height:30px;border-radius:50%;background:var(--grad)}

/* reviews */
.reviews{top:1965px;height:404px;background:linear-gradient(100deg,#4a4d50,#8f9396 50%,#54575a)}
.reviews .h2{color:#fff;top:85px;position:absolute}
.reviews .eyebrow{top:68px;position:absolute}
.avatar{position:absolute;left:575px;top:163px;width:50px;height:50px;border-radius:50%;background:#7d6d62;border:3px solid #fff}
.quote{top:228px;font-size:14.5px;line-height:21px;color:#fff}
.stars{top:285px;color:var(--green);font-size:11px;letter-spacing:3px}
.who{top:308px;color:#fff;font-size:10px;line-height:15px}

/* problem */
.problem{top:2369px;height:587px}
.col-h{position:absolute;top:231px;font-size:11px;font-weight:700;letter-spacing:1px;color:var(--teal)}
.row{position:absolute;display:flex;align-items:center;gap:14px;font-size:9.5px;line-height:13px}
.row.l{right:770px;text-align:right}
.row.r{left:768px}
.row .c{flex:none;width:50px;height:50px;border-radius:50%;background:var(--dark)}
.row .c.on{background:var(--teal)}
.row.l p{width:240px}
.row.r p{width:210px}
.circle-pic{left:479px;top:266px;width:240px;height:240px;border-radius:50%;background:linear-gradient(135deg,#f4f6f8,#b8c3cf);border:6px solid #fff;box-shadow:0 4px 18px rgba(0,0,0,.12)}

/* storage */
.storage{top:2956px;height:522px;background:linear-gradient(var(--light),#fff 70%)}
.trio{position:absolute;top:200px;left:330px;width:540px;display:flex;justify-content:space-between}
.tri{width:140px;text-align:center;font-size:9.5px;font-weight:600;color:var(--ink)}
.tri .ic{width:56px;height:56px;border-radius:50%;background:#fff;margin:0 auto 12px;box-shadow:0 2px 8px rgba(0,0,0,.12);position:relative}
.tri .ic.dk{background:var(--dark)}
.tri .ic i{position:absolute;left:20px;bottom:-6px;width:14px;height:14px;border-radius:50%;background:var(--teal)}
.boxes{position:absolute;top:352px;left:135px;display:flex;gap:11px}
.box{width:176px;height:137px;background:#fff;box-shadow:0 1px 6px rgba(0,0,0,.08);display:flex;flex-direction:column;align-items:center;justify-content:center;text-align:center;font-size:9.5px;font-weight:600;color:var(--ink);padding:0 18px;gap:10px}
.box.on{background:#3a3a3a;color:var(--green)}
.box i{width:14px;height:14px;border:2px solid var(--green);border-radius:2px}

/* news */
.news{top:3478px;height:426px}
.articles{position:absolute;top:160px;left:165px;display:flex;gap:30px}
.art{width:280px;padding:20px;font-size:9.5px;line-height:13px}
.art.on{box-shadow:0 2px 12px rgba(0,0,0,.12)}
.art .src{font-size:14px;font-weight:600;color:#999;margin-bottom:16px}
.art .src.blue{color:#1d3e8a}
.art h5{font-size:11px;color:var(--ink);font-weight:600;margin-bottom:4px}
.art .date{color:#bbb;font-size:8px;margin-top:14px}
.art .more{color:var(--teal);font-size:8px;margin-top:14px}
.arrow{position:absolute;top:230px;color:#bbb;font-size:20px}

/* contact */
.touch{top:3904px;height:257px;background:linear-gradient(100deg,#2a2c2e,#55595c 50%,#2a2c2e)}

/* footer */
.foot{top:4161px;height:320px;background:var(--dark);color:#aaa;font-size:9.5px}
.fcol{position:absolute;top:67px;line-height:17px}
.fcol h6{font-size:8.5px;letter-spacing:1px;color:#999;font-weight:600;margin-bottom:12px}
.fcol a{display:block;color:#fff;text-decoration:none}
.fcol.c3 span{display:block;color:#fff}
.news-in{margin-top:10px;width:220px;height:24px;border-radius:12px;background:#3d3d3d;font-size:8px;color:#777;padding:6px 12px}
.social{display:flex;gap:12px;justify-content:center;margin-top:8px}
.social i{width:14px;height:14px;border-radius:50%;background:#fff;display:block}
.social i.on{background:var(--teal)}
.copy{position:absolute;top:286px;left:129px;font-size:8px;color:#999}
.legal{position:absolute;top:286px;right:129px;font-size:8px;color:#fff;font-weight:600;display:flex;gap:20px}
</style>
</head>
<body>

<header class="hero">
  <div class="ph" role="img" aria-label="Photo of hands holding a tablet showing an X-ray image" style="inset:0"></div>
  <nav class="nav">
    <div class="logo">TORVA <i></i></div>
    <div class="menu"><span class="on">HOME</span><span>COMPANY</span><span>FAQ</span><span>NEWS ROOM</span><span>CONTACT</span></div>
    <div class="phone">&#9990; 1-833-GETORVA</div>
    <div class="login">LOGIN/REGISTER</div>
  </nav>
  <div class="abs center tag">TORVA BENEFITS <b>PATIENTS</b></div>
  <h1 class="center">Empower Patients &amp;<br>Healthcare Providers</h1>
  <div class="abs center sub">The first truly secure, nation-wide, interoperable diagnostic imaging and report sharing<br>eco-system.</div>
  <div class="abs center cta"><span class="btn">Explore More</span></div>
  <div class="scroll"></div>
</header>

<section class="think">
  <div class="ph pic" role="img" aria-label="Photo of a person walking through a data center server aisle"></div>
  <div class="play"></div>
  <div class="abs copy">
    <div class="eyebrow">Platform</div>
    <h3>Thinking Ahead</h3>
    <p>There are so many competing pressures on healthcare providers today: meaningful use, data security, managing costs and of course increasing revenue.</p>
    <p>Solving all of these issues can sometimes seem like a mine field... what systems should I buy, how do I ensure data security while exposing it in patient or physician portals, how can I maintain or reduce my costs while meeting all of these requirements.</p>
    <p>TORVA can help you meet these requirements through a revolutionary approach to the healthcare eco-system.</p>
  </div>
</section>

<section class="approach">
  <div class="abs center eyebrow" style="top:10px;color:#9fd3e3">Approach</div>
  <div class="steps">
    <div class="step"><div class="ic"><span></span></div><b>01</b>Increase revenue by extending your patient reach</div>
    <div class="step"><div class="ic"><span></span></div><b>02</b>Provides an instant return through cost savings</div>
    <div class="step"><div class="ic active">03</div>Adapts to all image provider environments; no system to install</div>
    <div class="step"><div class="ic"><span></span></div><b>04</b>Provides a free secure place where patients can participate</div>
    <div class="step"><div class="ic"><span></span></div><b>05</b>Provides a free secure place where physicians can improve quality of care</div>
    <div class="step"><div class="ic"><span></span></div><b>06</b>Provides a secure cloud based storage vault for images and reports</div>
  </div>
</section>

<section class="solution">
  <div class="bubble" style="top:-28px"><span></span></div>
  <div class="abs center eyebrow" style="top:70px">Solution</div>
  <div class="abs center h2" style="top:87px">A Revolutionary Centralized<br>Cloud-Based Platform</div>
  <div class="abs center lead" style="top:155px">Enabling healthcare providers, payers, radiology imaging companies &amp; patients with secure<br>access to real-time patient diagnostic images and reports sharing across organizational<br>boundaries.</div>
  <div class="cards">
    <div class="card photo1" role="img" aria-label="Photo of a radiologist beside a patient in a scanner"><div class="lbl">IMAGE PROVIDERS</div><div class="dot"></div></div>
    <div class="card mid">
      <h4>PHYSICIANS</h4>
      <ul>
        <li>Web-Based &amp; Easy To Use!</li>
        <li>Eliminate CDs That Are Difficult To Read</li>
        <li>Quick Access To Images &amp; Reports</li>
        <li>Automated Notification &amp; Alerts Systems</li>
        <li>Creates Flexibility In Remote/Telemedicine Capabilities</li>
        <li>Easily Download Patient Images &amp; Reports To Your EHR Or PACS System</li>
        <li>TORVA Improves The Quality Of Care To Your Patients</li>
      </ul>
      <div class="mini"></div>
    </div>
    <div class="card photo2" role="img" aria-label="Photo of a man with a coffee cup using a laptop"><div class="lbl">PATIENTS</div><div class="dot"></div></div>
  </div>
</section>

<section class="reviews" role="img" aria-label="Background photo of a patient resting in a hospital bed">
  <div class="eyebrow center">Testimonials</div>
  <div class="h2 center">Patient Reviews</div>
  <div class="avatar" role="img" aria-label="Reviewer portrait"></div>
  <div class="abs center quote">“I had an X-Ray taken by my Dr and was so thrilled that I did not have to pay for another<br>image when they referred me to another provider”</div>
  <div class="abs center stars">★★★★★</div>
  <div class="abs center who"><b>Daniel</b><br>Reeves</div>
</section>

<section class="problem">
  <div class="abs center eyebrow" style="top:68px">Problem / Solution</div>
  <div class="abs center h2" style="top:86px">Streamlined Diagnosis &amp;<br>Decision Making</div>
  <div class="abs center lead" style="top:153px">TORVA allows the ownership of the images to be in the Patient's hands and enables<br>interoperability between Diagnostic Imaging Centers, Patients and Physicians.</div>
  <div class="col-h" style="left:361px">PROBLEM</div>
  <div class="col-h" style="left:769px">SOLUTION</div>
  <div class="row l" style="top:256px"><p>No real-time solutions today for sharing radiology images and reports between physicians, imaging providers and patients</p><span class="c"></span></div>
  <div class="row l" style="top:322px"><p>Too much duplication of imaging</p><span class="c"></span></div>
  <div class="row l" style="top:388px"><p>No notification to the patient following physician review of image and report</p><span class="c"></span></div>
  <div class="row l" style="top:454px"><p>Too many manual processes today in order for providers to access patient images and reports</p><span class="c"></span></div>
  <div class="ph circle-pic" role="img" aria-label="Photo of a doctor holding a tablet"></div>
  <div class="row r" style="top:256px"><span class="c"></span><p>Secure Web-based Cloud platform that provides sharing images and reports</p></div>
  <div class="row r" style="top:322px"><span class="c on"></span><p>Eliminated localized storage costs</p></div>
  <div class="row r" style="top:388px"><span class="c"></span><p>Patient owns the image and report and optionally assigns rights to providers</p></div>
  <div class="row r" style="top:454px"><span class="c"></span><p>Provides secure audit trail</p></div>
</section>

<section class="storage">
  <div class="bubble" style="top:-28px"><span></span></div>
  <div class="abs center eyebrow" style="top:68px">Storage</div>
  <div class="abs center h2" style="top:86px">Disaster-Proof Your Data &amp;<br>Diagnostics With TORVA Storage</div>
  <div class="trio">
    <div class="tri"><div class="ic"><i style="background:#ccc"></i></div>1 + 2 = FREE</div>
    <div class="tri"><div class="ic dk"><i style="background:var(--green)"></i></div>STORAGE SOLUTIONS</div>
    <div class="tri"><div class="ic"><i></i></div>SOFTWARE</div>
  </div>
  <div class="abs center lead" style="top:310px">Server security has always been a concern but with large breaches in critical information, more healthcare providers are<br>taking extra disaster recovery measures than ever before.</div>
  <div class="boxes">
    <div class="box"><i></i>Simple, Scalable, Secure &amp; Shareable</div>
    <div class="box"><i></i>HIPAA Eligible Service</div>
    <div class="box on"><i style="border-radius:50%;background:var(--green)"></i>Partnered With Cold Archive</div>
    <div class="box"><i></i>99.9% Availability</div>
    <div class="box"><i></i>Modernize Your Business &amp; Streamline Storage Processes</div>
  </div>
</section>

<section class="news">
  <div class="abs center eyebrow" style="top:40px">News Room</div>
  <div class="abs center h2" style="top:60px">Industry Articles</div>
  <div class="abs center lead" style="top:98px">TORVA Press Releases</div>
  <div class="arrow" style="left:127px">‹</div>
  <div class="arrow" style="left:1058px">›</div>
  <div class="articles">
    <div class="art"><div class="src">NewsPulse Wire</div><h5>Lorem Ipsum Dolor</h5>Lorem Ipsum Is Simply Dummy Text Of The Printing And Typesetting Industry.<div class="date">May 29th, 2022</div></div>
    <div class="art on"><div class="src blue">TradeWire</div><h5>Lorem Ipsum Dolor</h5>Lorem Ipsum Is Simply Dummy Text Of The Printing And Typesetting Industry.<div class="more">Read More →</div></div>
    <div class="art"><div class="src">Clinic Daily</div><h5>Lorem Ipsum Dolor</h5>Lorem Ipsum Is Simply Dummy Text Of The Printing And Typesetting Industry.<div class="date">June 9th, 2022</div></div>
  </div>
  <div class="abs center" style="top:342px"><span class="btn">View All Articles</span></div>
</section>

<section class="touch" role="img" aria-label="Background photo of medical imaging equipment">
  <div class="bubble" style="top:-28px"><span></span></div>
  <div class="abs center eyebrow" style="top:70px">Support</div>
  <div class="abs center h2" style="top:88px;color:#fff">Get In Touch</div>
  <div class="abs center lead" style="top:128px;color:#fff">Find out how TORVA can help you</div>
  <div class="abs center" style="top:160px"><span class="btn">✉ Contact Us</span></div>
</section>

<footer class="foot">
  <div class="fcol" style="left:190px;top:72px;text-align:center">
    <div style="font-size:24px;font-weight:700;color:var(--green)">TORVA</div>
    <div style="margin-top:10px">Follow Us:</div>
    <div class="social"><i></i><i class="on"></i><i></i></div>
  </div>
  <div class="fcol" style="left:369px"><h6>ABOUT</h6><a>Home</a><a>Company</a><a>FAQ</a><a>News Room</a><a>Contact</a></div>
  <div class="fcol" style="left:529px"><h6>PLATFORM</h6><a>Login</a><a>Register</a><a>Guest Access</a><a>User Forum</a></div>
  <div class="fcol c3" style="left:689px;line-height:13px"><h6>CONTACT</h6>Address:<span>118 Linden Ave,</span><span>Dayton Falls, Ohio 45000</span><br>Phone:<span>1-833-GETORVA</span><br>Email:<span>info@getorva.com</span></div>
  <div class="fcol" style="left:849px;line-height:13px;width:230px"><h6>NEWSLETTER</h6>Subscribe to our emailing list, lorem ipsum is simply dummy text of the printing and typesetting industry.<div class="news-in">Your Email Address</div></div>
  <div class="copy">© Copyright 2022 Northbeam Labs Inc. All Rights Reserved</div>
  <div class="legal"><span>PRIVACY POLICY</span><span>TERMS &amp; CONDITIONS</span></div>
</footer>

</body>
</html>
```